Need to design a business card with logo

Hellow
we are a company ,
PT REKA LINTAS MANDIRI
looking for design of name card.
what we do is property development and management.
design preferable professional corporate look and feel.
corporate. color, pantone colour 289
information required is
company name " Reka Lintas Mandiri"
person name eg " Peter Hollis"
person title eg "secret agent"
address: 9 kestrel road , jakarta, indonesia
phone : +6221 5906471
mobile : 0813 294 615
email : peter@hollistran.com
website: www.peterhol.com
if you want to include logo in the design you are welcome and appreciated , or you can simply use the company name as the logo.
thanks
corporate , business person , show events, exhibition events ,etc
Business

```html
<!DOCTYPE html>
<html lang="en">
<head>
<meta charset="utf-8">
<title>Reka Lintas Mandiri – Business Card</title>
<link href="https://fonts.googleapis.com/css2?family=Archivo:wght@800&family=Arimo&family=Open+Sans:wght@400&display=swap" rel="stylesheet">
<style>
  :root {
    --navy: #23284f;
    --ink: #1d1d22;
    --paper: #ffffff;
    --backdrop: #e9e7e3;
  }
  html, body {
    margin: 0;
    width: 1200px;
    height: 871px;
    overflow: hidden;
    background: var(--backdrop);
  }
  .canvas {
    position: relative;
    width: 1200px;
    height: 871px;
  }
  .card {
    position: absolute;
    top: 147px;
    width: 330px;
    height: 577px;
    background: var(--paper);
    box-shadow: 0 2px 10px rgba(0,0,0,0.12);
    overflow: hidden;
  }
  .card--back { left: 235px; }
  .card--front { left: 635px; }

  .card--back svg { display: block; }
  .back-name {
    font-family: "Archivo", "Arial Black", sans-serif;
    font-weight: 800;
    font-size: 25px;
    fill: var(--paper);
    letter-spacing: 0.5px;
  }

  .company {
    position: absolute;
    top: 96px;
    left: 0;
    right: 0;
    margin: 0;
    text-align: center;
    font-family: "Archivo", "Arial Black", sans-serif;
    font-weight: 800;
    font-size: 27px;
    color: var(--navy);
  }
  .side-bar {
    position: absolute;
    left: 0;
    top: 296px;
    width: 44px;
    height: 168px;
    background: var(--navy);
  }
  .person {
    position: absolute;
    left: 92px;
    top: 268px;
  }
  .person__name {
    margin: 0;
    font-family: "Arimo", Arial, sans-serif;
    font-size: 28px;
    color: var(--ink);
    line-height: 1.05;
  }
  .person__title {
    margin: 3px 0 0 6px;
    font-family: "Open Sans", sans-serif;
    font-size: 14px;
    color: var(--navy);
  }
  .contacts {
    position: absolute;
    left: 92px;
    top: 370px;
    margin: 0;
    padding: 0;
    list-style: none;
    font-family: "Open Sans", sans-serif;
    font-size: 15px;
    color: var(--ink);
    line-height: 1.3;
  }
  .contacts__group {
    position: relative;
    padding-left: 22px;
    margin-bottom: 18px;
  }
  .contacts__group::before {
    content: "";
    position: absolute;
    left: 0;
    top: 4px;
    bottom: 2px;
    width: 5px;
    border-radius: 3px;
    background: var(--navy);
  }
  .contacts__group span { display: block; }
</style>
</head>
<body>
<div class="canvas">

  <div class="card card--back">
    <svg width="330" height="577" viewBox="0 0 330 577" aria-label="Card back with company band">
      <polygon points="0,235 330,120 330,270 0,385" fill="var(--navy)"/>
      <text class="back-name" x="165" y="262" text-anchor="middle" transform="rotate(-19 165 252)">REKA LINTAS MANDIRI</text>
    </svg>
  </div>

  <div class="card card--front">
    <h1 class="company">Reka Lintas Mandiri</h1>
    <div class="side-bar"></div>
    <div class="person">
      <p class="person__name">Peter Hollis</p>
      <p class="person__title">secret agent</p>
    </div>
    <ul class="contacts">
      <li class="contacts__group">
        <span>+6221 5906471</span>
        <span>0813 294 615</span>
      </li>
      <li class="contacts__group">
        <span>peter@hollistran.com</span>
        <span>www.peterhol.com</span>
      </li>
      <li class="contacts__group">
        <span>9 kestrel road , jakarta, indonesia</span>
      </li>
    </ul>
  </div>

</div>
</body>
</html>
```